Aviation security consulting company needs a website

We need a website design for Brell Ostavik, and aviation security consulting company. Brell Ostavik (www.brellostavik.example) is an aviation security consulting company that works with government and industry stakeholders in over 60 countries on aviation security strategy, governance, and oversight at the regulatory and operational level.
Brell Ostavik is strongly internationally focused.
The website required should be simple, corporate, serious, and communicate professionalism, reliability and honesty. We are trying to give the company a feeling of being well established.
The attached files include the company logo, along with examples of company web page styles that we like.
The Brell Ostavik website need only be around five pages long (landing page, who we are, our services, our clients, contact), though don't feel limited to only five pages.
The existing website (www.brellostavik.example) was rushed and put together using Wix. We don't love the existing website as it looks too amateur, so don't use it as a template.
There is no requirement for any online sales tools to be included in the site. The site is purely informational, with the option of people making contact via email.

```html
<!DOCTYPE html>
<html lang="en">
<head>
<meta charset="utf-8">
<title>Brell Ostavik — Aviation Security Consulting</title>
<link href="https://fonts.googleapis.com/css2?family=Open+Sans:ital,wght@0,300;0,400;0,600;1,400&display=swap" rel="stylesheet">
<style>
:root{
  --blue:#3aa7ea;
  --navy:#1d2a4f;
  --text:#333;
  --muted:#8a8a8a;
  --line:#d6d6d6;
  --panel:#f4f4f4;
  --footer:#4d4d4d;
  --footer-bar:#444;
  --footer-text:#c9c9c9;
  --white:#fff;
}
*{box-sizing:border-box;margin:0;padding:0}
html,body{width:1042px;height:1200px;overflow:hidden;background:var(--white)}
body{font-family:"Open Sans",Arial,sans-serif;color:var(--text);position:relative}
.abs{position:absolute}

/* header */
.site-header{position:absolute;left:0;top:0;width:1042px;height:62px;background:var(--white)}
.brand{position:absolute;left:164px;top:16px;display:flex;align-items:center;gap:7px}
.brand-mark{width:24px;height:24px;background:var(--navy)}
.brand-name{font-size:17px;font-weight:600;color:var(--navy);line-height:1}
.brand-tag{font-size:7.5px;letter-spacing:1.4px;color:var(--navy);margin-top:2px}
.main-nav{position:absolute;top:0;left:597px;display:flex;height:62px}
.main-nav a{display:flex;align-items:center;height:62px;padding:0 11px;font-size:10.5px;color:var(--navy);text-decoration:none;margin-right:5px}
.main-nav a.active{background:var(--blue);color:var(--white);padding:0 11.5px}

/* hero */
.hero{position:absolute;left:0;top:62px;width:1042px;height:372px;
  background:linear-gradient(180deg,#5a6a9e 0%,#b06a8e 30%,#f07070 60%,#f58d7c 100%)}
.hero-caption{position:absolute;left:164px;top:201px;width:306px;height:110px;background:rgba(60,60,70,.72);
  color:var(--white);font-size:13.5px;line-height:18px;padding:14px 7px 0 7px}

/* section headings */
.sec-title{display:flex;align-items:center;font-size:12.5px;color:#666}
.sec-title::after{content:"";flex:1;height:4px;margin-left:5px;border-top:1px solid var(--line);border-bottom:1px solid var(--line)}

.why{left:163px;top:474px;width:350px}
.why-box{left:164px;top:497px;width:349px;height:222px;border:1px solid #999;padding:13px 13px;
  font-size:10px;font-weight:300;color:#666;line-height:18px}
.why-box p+p{margin-top:18px}

.offer{left:524px;top:474px;width:354px}
.offer-bar{left:524px;top:495px;width:354px;height:21px;background:var(--blue);color:var(--white);
  font-size:10px;font-weight:600;text-align:center;line-height:21px;padding-right:90px}
.offer-panel{left:524px;top:516px;width:354px;height:203px;background:var(--panel);padding:10px 14px;
  font-size:10px;font-weight:300;color:#666;line-height:18px}
.offer-list{list-style:none;margin-top:14px}
.offer-list li{display:flex;align-items:center;gap:9px;height:22px}
.offer-list svg{width:7px;height:10px}

/* projects */
.projects{left:163px;top:732px;width:717px;height:199px;background:#f7f7f7;border:1px solid #e2e2e2}
.projects-title{left:198px;top:743px;width:597px}
.dots{left:828px;top:746px;display:flex;gap:3px}
.dots span{width:11px;height:11px;border-radius:50%;border:1px solid #999;background:var(--white)}
.project{position:absolute;top:773px;width:155px}
.project .thumb{width:155px;height:109px}
.project h3{font-size:12.5px;font-weight:400;color:var(--blue);margin-top:4px;line-height:16px}
.project .date{font-size:10.5px;font-style:italic;color:#666;line-height:15px}

/* footer */
.site-footer{left:0;top:978px;width:1042px;height:176px;background:var(--footer)}
.fcol{position:absolute;top:995px}
.fcol h4{font-size:12.5px;font-weight:600;color:var(--white);margin-bottom:8px}
.fcol p{font-size:10px;font-weight:300;color:var(--footer-text);line-height:17.8px}
.flinks{list-style:none}
.flinks li{font-size:10.5px;color:var(--blue);line-height:22.2px;display:flex;align-items:center;gap:5px}
.flinks svg{width:5px;height:8px}
.contact-row{font-size:10.5px;color:var(--footer-text);line-height:22.4px}
.contact-row a{color:var(--blue);text-decoration:none}

.footer-bar{left:0;top:1154px;width:1042px;height:46px;background:var(--footer-bar);border-top:1px solid #3a3a3a}
.footer-brand{left:164px;top:1163px;display:flex;align-items:center;gap:6px}
.footer-brand .brand-mark{background:#ddd;width:22px;height:22px}
.footer-brand .brand-name{color:#ddd;font-size:15px}
.footer-brand .brand-tag{color:#bbb;font-size:6.5px}
.copyright{left:394px;top:1169px;font-size:10.5px;color:var(--white)}
.footer-nav{left:648px;top:1171px;display:flex;gap:11px;font-size:8.5px}
.footer-nav a{color:var(--blue);text-decoration:none}
</style>
</head>
<body>

<header class="site-header">
  <div class="brand">
    <div class="brand-mark"></div>
    <div>
      <div class="brand-name">Brell Ostavik</div>
      <div class="brand-tag">aviation security consulting</div>
    </div>
  </div>
  <nav class="main-nav">
    <a class="active" href="#">HOME</a>
    <a href="#">WHO WE ARE</a>
    <a href="#">SERVICES</a>
    <a href="#">CONTACT</a>
  </nav>
</header>

<section class="hero" role="img" aria-label="Passenger jet flying toward the viewer against a pink and violet sunset sky with contrails">
  <div class="hero-caption">We work with government and industry stakeholders in over 60 countries, providing aviation security strategy and oversight at the regulatory and operational level.</div>
</section>

<h2 class="abs sec-title why">Why Us?</h2>
<div class="abs why-box">
  <p>Artisan cronut trust fund stumptown, vegan letterpress microdosing fingerstache authentic viral single-origin coffee slow-carb. Small batch pitchfork authentic paleo. Man braid lo-fi synth kombucha kickstarter man bun post-ironic, 8-bit pickled.</p>
  <p>Tattooed fap sustainable cornhole, microdosing put a bird on it chill-wave literally retro mumblecore 8-bit photo booth. Selvage truffaut celiac, ennui wayfarers lo-fi flexitarian letterpress kickstarter hoodie etsy hashtag biodiesel polaroid. Celiac sriracha portland, XOXO VHS fanny pack PBR&amp;B humblebrag deep v messenger bag vice venmo typewriter bespoke cliche.</p>
</div>

<h2 class="abs sec-title offer">We Offer</h2>
<div class="abs offer-bar">SUB HEADING</div>
<div class="abs offer-panel">
  <p>Artisan cronut trust fund stumptown, vegan letterpress microdosing fingerstache authentic viral single-origin coffee slow-carb. Small batch pitchfork authentic paleo. Man braid lo-fi synth kombucha kickstarter man bun post-ironic, 8-bit pickled.</p>
  <ul class="offer-list">
    <li><svg viewBox="0 0 7 10"><path d="M1 1l4 4-4 4" fill="none" stroke="#3aa7ea" stroke-width="1.3"/></svg>Lorem ipsum dolor sit amet</li>
    <li><svg viewBox="0 0 7 10"><path d="M1 1l4 4-4 4" fill="none" stroke="#3aa7ea" stroke-width="1.3"/></svg>Lorem ipsum dolor sit amet</li>
    <li><svg viewBox="0 0 7 10"><path d="M1 1l4 4-4 4" fill="none" stroke="#3aa7ea" stroke-width="1.3"/></svg>Lorem ipsum dolor sit amet</li>
    <li><svg viewBox="0 0 7 10"><path d="M1 1l4 4-4 4" fill="none" stroke="#3aa7ea" stroke-width="1.3"/></svg>Lorem ipsum dolor sit amet</li>
  </ul>
</div>

<section class="abs projects"></section>
<h2 class="abs sec-title projects-title">Recent Projects</h2>
<div class="abs dots"><span></span><span></span><span></span></div>

<article class="project" style="left:198px">
  <div class="thumb" role="img" aria-label="Two colleagues reviewing documents at a desk" style="background:linear-gradient(135deg,#4a5860,#9a8a78 60%,#c9c2b5)"></div>
  <h3>Project Heading</h3><p class="date">Created June 2106</p>
</article>
<article class="project" style="left:362px">
  <div class="thumb" role="img" aria-label="Airliner parked on an airport apron under a cloudy sky" style="background:linear-gradient(180deg,#6d7e92,#b3b0aa 55%,#5a5f66)"></div>
  <h3>Project Heading</h3><p class="date">Created June 2106</p>
</article>
<article class="project" style="left:526px">
  <div class="thumb" role="img" aria-label="Hand touching a glowing data screen" style="background:linear-gradient(160deg,#1d1a3a,#3a6ab8 55%,#b04aa0)"></div>
  <h3>Project Heading</h3><p class="date">Created June 2106</p>
</article>
<article class="project" style="left:690px">
  <div class="thumb" role="img" aria-label="Abstract blue digital network of connected points" style="background:radial-gradient(circle at 60% 50%,#2e5a8e,#0f1f3a 75%)"></div>
  <h3>Project Heading</h3><p class="date">Created June 2106</p>
</article>

<footer class="abs site-footer"></footer>
<div class="fcol" style="left:164px;width:190px">
  <h4>About Us</h4>
  <p>Lorem ipsum dolor sit amet, consecte-tur adipiscing elit. Donec rutrum ultrices aliquet. Sed euismod tincidunt finibus. Sed nec purus mauris. Cras porttitor lacus sit amet elit vulputate, eu rutrum diam rutrum.</p>
</div>
<div class="fcol" style="left:408px">
  <h4>Links</h4>
  <ul class="flinks">
    <li><svg viewBox="0 0 5 8"><path d="M1 1l3 3-3 3" fill="none" stroke="#c9c9c9"/></svg>Lorem ipsum dolor sit amet</li>
    <li><svg viewBox="0 0 5 8"><path d="M1 1l3 3-3 3" fill="none" stroke="#c9c9c9"/></svg>Lorem ipsum dolor sit amet</li>
    <li><svg viewBox="0 0 5 8"><path d="M1 1l3 3-3 3" fill="none" stroke="#c9c9c9"/></svg>Lorem ipsum dolor sit amet</li>
    <li><svg viewBox="0 0 5 8"><path d="M1 1l3 3-3 3" fill="none" stroke="#c9c9c9"/></svg>Lorem ipsum dolor sit amet</li>
    <li><svg viewBox="0 0 5 8"><path d="M1 1l3 3-3 3" fill="none" stroke="#c9c9c9"/></svg>Lorem ipsum dolor sit amet</li>
  </ul>
</div>
<div class="fcol" style="left:648px">
  <h4>Contact Information</h4>
  <p class="contact-row" style="line-height:17.6px">Address: 123 Street Name<br>City, CA 90017</p>
  <p class="contact-row" style="margin-top:4px">Tel:&nbsp;&nbsp;&nbsp;&nbsp;&nbsp;&nbsp;&nbsp;+(090) 123 456 789</p>
  <p class="contact-row">Fax:&nbsp;&nbsp;&nbsp;&nbsp;&nbsp;&nbsp;&nbsp;+(090) 123 456 789</p>
  <p class="contact-row">Email:&nbsp;&nbsp;&nbsp;&nbsp;<a href="#">inof@email.com</a></p>
</div>

<div class="abs footer-bar"></div>
<div class="abs footer-brand">
  <div class="brand-mark"></div>
  <div>
    <div class="brand-name">Brell Ostavik</div>
    <div class="brand-tag">aviation security consulting</div>
  </div>
</div>
<p class="abs copyright">Copyright 2016. All Rights Reserved</p>
<nav class="abs footer-nav"><a href="#">About us</a><a href="#">Sitemap</a><a href="#">Support</a></nav>

</body>
</html>
```